quiet meadow therapy (QMT)

I need to build a website for my therapy business.
There are two parts to the website
on the landing page; they choose whether they are therapists making a referral or patients needing more information.
After that, they are taken to their respective pages.
There is the textual information and a referral form on the therapist page, and on the patient page, the text is a bit different, and there will be a booking page on the patient page.
Visually minimal, it's a therapeutic website. I want it clean, clinical, and modern
colors: greenish blue or maybe orangish
PHP/html code
Updates

Hi everyone
I'm very sorry for the lack of responses to your designs. I am trying to work it out, but this platform has been a challenge for me.
I appreciate everyone's efforts, and I am unsure how to rate designs and move forward with the ones I like. There is a 5-star rating, but I don't understand how I'm supposed to politely say that it is not it without feeling like I'm going to affect someone's future rating negatively.
Please understand me. Thank you

Designs look the same

Target Market(s)

therapy and stress management

Industry/Entity Type

stress management therapy

Coding

Coded - Design and coding required

Number of Pages Required

5+ page

Font styles to use
Serif

Colors
0094D4
00A9DD
6FCCEA
C7EBF8
E9F6FB
00AB8E
00BBA5
67D7C9
C6EFE9
E9F9F6

Requirements
Must have
• landing page that that have 2 options. one for therapist another for patient

```html
<!DOCTYPE html>
<html lang="en">
<head>
<meta charset="utf-8">
<title>QMT – Quiet Meadow Therapy</title>
<link rel="stylesheet" href="https://fonts.googleapis.com/css2?family=Poppins:wght@400;500;600;700;800&display=swap">
<style>
:root{
  --teal:#16b3a3;
  --teal-soft:#8fd3cc;
  --teal-pale:#e9f6f5;
  --orange:#f7931e;
  --peach:#fdf0e1;
  --ink:#231f20;
  --text:#4a4a4a;
  --muted:#9a9a9a;
  --field:#efefef;
  --white:#ffffff;
}
*{margin:0;padding:0;box-sizing:border-box}
html,body{width:1200px;height:3684px;overflow:hidden;background:var(--white)}
body{position:relative;font-family:"Poppins",sans-serif;color:var(--ink)}
.abs{position:absolute}
.logo{display:flex;align-items:center;gap:14px}
.logo-mark{width:46px;height:46px;border-radius:50%;background:var(--teal)}
.logo-name{font-size:52px;font-weight:500;letter-spacing:18px;line-height:1;color:var(--ink)}
.logo-tag{font-size:12.5px;font-weight:600;letter-spacing:1.6px;color:var(--orange);margin-top:8px}
.nav{display:flex;gap:38px;font-size:12.5px;font-weight:500;text-transform:uppercase;color:var(--ink)}
.hero-title{font-size:57px;font-weight:800;line-height:66px;text-transform:uppercase}
.hero-title .accent{color:var(--orange)}
.lead{font-size:15px;line-height:25px;color:var(--text)}
.btn{display:inline-flex;align-items:center;justify-content:center;background:var(--orange);color:var(--white);font-weight:700;font-size:14px;text-transform:uppercase;border-radius:0 24px 24px 24px}
.btn-alt{background:var(--teal)}
.h2{font-size:40px;font-weight:800;line-height:45px;text-transform:uppercase}
.eyebrow{font-size:16px;font-weight:600;color:var(--orange);text-transform:uppercase}
.body{font-size:14.5px;line-height:25px;color:var(--text)}
.ph{display:block}
.card{position:absolute;top:1979px;width:240px;height:322px;background:var(--white);border-radius:14px;box-shadow:0 10px 30px rgba(0,0,0,.08);text-align:center}
.card-icon{position:absolute;left:71px;top:26px;width:98px;height:108px}
.card-title{position:absolute;top:163px;width:100%;font-size:15px;font-weight:600;text-transform:uppercase}
.card-text{position:absolute;top:197px;left:26px;right:26px;font-size:13.5px;line-height:20px;color:var(--text)}
.card-rule{position:absolute;top:275px;left:24px;right:24px;height:1px;background:#ececec}
.card-more{position:absolute;top:290px;width:100%;font-size:12px;font-weight:600;color:var(--muted);text-transform:uppercase}
.label{font-size:11px;font-weight:600;text-transform:uppercase}
.field{position:absolute;background:var(--field);font-size:12px;color:#888;padding-left:15px;display:flex;align-items:center}
.contact{position:absolute;top:2964px;width:340px;text-align:center}
.contact-icon{width:66px;height:66px;border-radius:50%;margin:0 auto;display:flex;align-items:center;justify-content:center}
.contact-label{font-size:20px;color:var(--text);margin-top:12px}
.contact-value{font-size:23px;font-weight:500;margin-top:2px;color:var(--ink)}
.footer-nav{display:flex;gap:38px;font-size:12.5px;font-weight:500;text-transform:uppercase;color:var(--white)}
.social{display:flex;gap:5px}
.social span{width:46px;height:46px;border-radius:50%;background:#3a3637;display:block}
</style>
</head>
<body>

<header>
  <div class="abs" style="left:89px;top:24px">
    <div class="logo"><span class="logo-mark"></span><span class="logo-name">QMT</span></div>
    <div class="logo-tag">QUIET MEADOW THERAPY</div>
  </div>
  <nav class="abs nav" style="left:563px;top:55px">
    <span>Home</span><span>Therapy</span><span>What is it?</span><span>Types of therapy</span><span>Referral form</span>
  </nav>
</header>

<section class="hero">
  <svg class="abs" style="left:0;top:0" width="1200" height="760">
    <path d="M640 172 C700 270 812 360 812 500 A172 172 0 0 1 468 500 C468 360 580 270 640 172Z" fill="var(--teal-pale)"/>
    <circle cx="940" cy="322" r="200" fill="var(--teal-soft)"/>
    <circle cx="940" cy="515" r="205" fill="var(--teal)" opacity=".85"/>
    <path d="M922 226 L940 198 L958 226Z" fill="var(--teal)"/>
    <path d="M922 605 L940 634 L958 605Z" fill="var(--teal)"/>
  </svg>
  <div class="abs ph" role="img" aria-label="Therapist writing notes on a clipboard while seated in a bright room" style="left:784px;top:227px;width:316px;height:378px;background:linear-gradient(160deg,#e8e4df,#d9d2c9 55%,#c9874e);box-shadow:0 10px 25px rgba(0,0,0,.15)"></div>
  <h1 class="abs hero-title" style="left:89px;top:294px">Best online<br><span class="accent">therapy</span> services<br>and therapists</h1>
  <p class="abs lead" style="left:89px;top:507px;width:540px">QMT is the global leader in providing online therapy &amp; virtual mental health services to people that deserve to improve</p>
  <div class="abs" style="left:89px;top:586px;display:flex;gap:14px">
    <span class="btn" style="width:180px;height:46px">For therapists</span>
    <span class="btn btn-alt" style="width:180px;height:46px">For patients</span>
  </div>
</section>

<section>
  <svg class="abs" style="left:110px;top:850px" width="460" height="400">
    <path d="M20 150 C10 60 120 40 200 70 C300 100 340 0 420 30 C470 60 460 150 430 190 C380 260 330 330 230 320 C140 310 30 260 20 150Z" fill="#e5f3f8"/>
    <ellipse cx="290" cy="330" rx="120" ry="45" fill="#e8f6f2"/>
  </svg>
  <div class="abs ph" role="img" aria-label="Woman smiling while using her phone" style="left:155px;top:866px;width:148px;height:148px;border-radius:50%;background:linear-gradient(160deg,#e6e2da,#b9a999);border:4px solid #fff"></div>
  <div class="abs ph" role="img" aria-label="Hands typing on a laptop" style="left:250px;top:977px;width:262px;height:176px;background:linear-gradient(140deg,#c89456,#7b4e2a 60%,#3a2a20);border-top:14px solid #f4f4f4;box-shadow:0 8px 22px rgba(0,0,0,.12)"></div>
  <div class="abs ph" role="img" aria-label="Phone screen showing a chat conversation" style="left:186px;top:1065px;width:80px;height:165px;background:linear-gradient(#fafafa,#eef2f6);border:2px solid #e4e4e4;border-radius:8px"></div>

  <h2 class="abs h2" style="left:603px;top:797px">Online therapy</h2>
  <p class="abs body" style="left:603px;top:859px;width:465px">Aenean sollicitudin, lorem quis bibendum auctor, nisi elit consequat ipsum, nec sagittis sem nibh id elit. Duis sed odio sit amet nibh vulputate cursus a sit amet mauris. Morbi accumsan ipsum velit. Nam nec tellus a odio tincidunt auctor a ornare odio. Sed non mauris vitae erat consequat auctor eu in elit. Class aptent taciti sociosqu ad litora torquent per conubia nostra, per inceptos himenaeos mauris in erat justo.</p>
  <p class="abs body" style="left:603px;top:1059px;width:465px">Nullam ac urna eu felis dapibus condimentum sit amet a augue. Sed non neque elit. Sed ut imperdiet nisi. Proin condimentum fermentum nunc. Etiam pharetra, erat sed fermentum feugiat, velit mauris egestas quam, ut aliquam massa nisl quis neque. Suspendisse in orci enim.</p>
</section>

<svg class="abs" style="left:0;top:1600px" width="1200" height="525">
  <path d="M0 52 C140 180 300 235 420 230 C720 215 980 0 1200 70 L1200 525 L0 525Z" fill="var(--teal)"/>
</svg>

<section>
  <p class="abs eyebrow" style="left:86px;top:1332px">What is it?</p>
  <h2 class="abs h2" style="left:86px;top:1368px">Online therapy<br>with QMT</h2>
  <p class="abs body" style="left:86px;top:1474px;width:470px">Aenean sollicitudin, lorem quis bibendum auctor, nisi elit consequat ipsum, nec sagittis sem nibh id elit. Duis sed odio sit amet nibh vulputate cursus a sit amet mauris. Morbi accumsan ipsum velit. Nam nec tellus a odio tincidunt auctor a ornare odio. Sed non mauris vitae erat consequat auctor eu in elit. Class aptent taciti sociosqu ad litora torquent per conubia nostra, per inceptos himenaeos mauris in erat justo.</p>
  <svg class="abs" style="left:0;top:0" width="1200" height="1860" role="img" aria-label="Therapist taking notes during a session with a client on a sofa">
    <defs><linearGradient id="sessionTone" x1="0" y1="0" x2="1" y2="1"><stop offset="0" stop-color="#e4e4e4"/><stop offset=".6" stop-color="#c9c3bd"/><stop offset="1" stop-color="#9b8a7c"/></linearGradient></defs>
    <path d="M907 1247 C960 1330 1111 1420 1111 1565 A254 254 0 0 1 735 1795 L731 1830 L712 1780 A254 254 0 0 1 660 1530 C740 1410 860 1340 907 1247Z" fill="url(#sessionTone)"/>
  </svg>
</section>

<section>
  <h2 class="abs h2" style="left:0;width:1200px;top:1898px;text-align:center;color:var(--white)">Types of therapy QMT</h2>

  <article class="card" style="left:89px">
    <svg class="card-icon" role="img" aria-label="Psychotherapy icon" viewBox="0 0 98 108"><path d="M49 108 L30 90 A49 49 0 1 1 68 90Z" fill="var(--peach)"/></svg>
    <h3 class="card-title">Psychotherapy</h3>
    <p class="card-text">Sagittis sem nibh id elit Duis sed odio sit amet nibh vulputate cursus a sit</p>
    <div class="card-rule"></div><p class="card-more">Read more</p>
  </article>
  <article class="card" style="left:350px">
    <svg class="card-icon" role="img" aria-label="EMDR therapy icon" viewBox="0 0 98 108"><path d="M49 108 L30 90 A49 49 0 1 1 68 90Z" fill="var(--peach)"/></svg>
    <h3 class="card-title">EMDR therapy</h3>
    <p class="card-text">Sagittis sem nibh id elit Duis sed odio sit amet nibh vulputate cursus a sit</p>
    <div class="card-rule"></div><p class="card-more">Read more</p>
  </article>
  <article class="card" style="left:611px">
    <svg class="card-icon" role="img" aria-label="Couples therapy icon" viewBox="0 0 98 108"><path d="M49 108 L30 90 A49 49 0 1 1 68 90Z" fill="var(--peach)"/></svg>
    <h3 class="card-title">Couples therapy</h3>
    <p class="card-text">Sagittis sem nibh id elit Duis sed odio sit amet nibh vulputate cursus a sit</p>
    <div class="card-rule"></div><p class="card-more">Read more</p>
  </article>
  <article class="card" style="left:871px">
    <svg class="card-icon" role="img" aria-label="Trauma therapy icon" viewBox="0 0 98 108"><path d="M49 108 L30 90 A49 49 0 1 1 68 90Z" fill="var(--peach)"/></svg>
    <h3 class="card-title">Trauma therapy</h3>
    <p class="card-text">Sagittis sem nibh id elit Duis sed odio sit amet nibh vulputate cursus a sit</p>
    <div class="card-rule"></div><p class="card-more">Read more</p>
  </article>
</section>

<section>
  <div class="abs ph" role="img" aria-label="Man reading a book in a grey armchair beside a small side table with a plant" style="left:57px;top:2345px;width:586px;height:558px;background:radial-gradient(ellipse at 50% 55%,#dfe6ea 0%,#eef1f3 45%,#ffffff 75%)"></div>
  <h2 class="abs h2" style="left:704px;top:2398px">Therapists<br>referral form</h2>

  <span class="abs label" style="left:706px;top:2520px">Name*</span>
  <span class="abs label" style="left:913px;top:2520px">Email*</span>
  <div class="field" style="left:709px;top:2541px;width:198px;height:40px">Enter your name</div>
  <div class="field" style="left:912px;top:2541px;width:198px;height:40px">Enter your email</div>

  <span class="abs label" style="left:706px;top:2589px">Phone*</span>
  <span class="abs label" style="left:913px;top:2589px">Date*</span>
  <div class="field" style="left:709px;top:2610px;width:198px;height:40px">Enter phone number</div>
  <div class="field" style="left:912px;top:2610px;width:198px;height:40px">Select date
    <svg class="abs" style="right:15px;top:16px" width="9" height="6" viewBox="0 0 9 6"><path d="M1 1l3.5 3.5L8 1" fill="none" stroke="#333" stroke-width="1.5"/></svg>
  </div>

  <span class="abs label" style="left:706px;top:2664px">Phone*</span>
  <div class="field" style="left:709px;top:2684px;width:401px;height:112px;align-items:flex-start;padding-top:14px">Type your text...</div>

  <div class="abs btn" style="left:709px;top:2824px;width:401px;height:53px;font-size:16px;border-radius:0 26px 26px 26px">Submit now
    <svg class="abs" style="right:20px;top:17px" width="19" height="19" viewBox="0 0 24 24"><path d="M2 11 L22 2 L15 22 L11 13Z" fill="none" stroke="#fff" stroke-width="2.4" stroke-linejoin="round"/><path d="M11 13 L22 2" stroke="#fff" stroke-width="2.4"/></svg>
  </div>
</section>

<section>
  <div class="contact" style="left:107px">
    <div class="contact-icon" style="background:var(--teal)">
      <svg width="24" height="24" viewBox="0 0 24 24"><path d="M6.6 10.8a15 15 0 0 0 6.6 6.6l2.2-2.2c.3-.3.7-.4 1-.2 1.1.4 2.3.6 3.6.6.6 0 1 .4 1 1V20c0 .6-.4 1-1 1A17 17 0 0 1 3 4c0-.6.4-1 1-1h3.5c.6 0 1 .4 1 1 0 1.3.2 2.5.6 3.6.1.3 0 .7-.2 1Z" fill="#fff"/></svg>
    </div>
    <p class="contact-label">Phone:</p>
    <p class="contact-value">+00 555 0142 7700</p>
  </div>
  <div class="contact" style="left:425px">
    <div class="contact-icon" style="background:var(--orange)">
      <svg width="22" height="26" viewBox="0 0 22 26"><path d="M11 0C5 0 1 4.5 1 10c0 7 10 16 10 16s10-9 10-16C21 4.5 17 0 11 0Z" fill="#fff"/><circle cx="11" cy="10" r="3.6" fill="var(--orange)"/></svg>
    </div>
    <p class="contact-label">Address:</p>
    <p class="contact-value">Some goes address here</p>
  </div>
  <div class="contact" style="left:742px">
    <div class="contact-icon" style="background:var(--ink)">
      <svg width="24" height="18" viewBox="0 0 24 18"><rect x="0" y="0" width="24" height="18" rx="2" fill="#fff"/><path d="M1 2 L12 10 L23 2" fill="none" stroke="var(--ink)" stroke-width="2"/></svg>
    </div>
    <p class="contact-label">Email:</p>
    <p class="contact-value" style="font-size:20px;margin-top:4px">hello@quietmeadowmail.com</p>
  </div>
</section>

<footer>
  <svg class="abs" style="left:0;top:3190px" width="1200" height="494">
    <path d="M0 273 C200 60 420 10 600 12 C800 14 1040 90 1200 260 L1200 494 L0 494Z" fill="var(--orange)"/>
    <path d="M0 320 C200 100 420 48 600 48 C820 48 1040 130 1200 290 L1200 494 L0 494Z" fill="var(--ink)"/>
  </svg>
  <div class="abs" style="left:0;width:1200px;top:3350px;display:flex;flex-direction:column;align-items:center">
    <div class="logo"><span class="logo-mark"></span><span class="logo-name" style="color:var(--white)">QMT</span></div>
    <div class="logo-tag">QUIET MEADOW THERAPY</div>
  </div>
  <nav class="abs footer-nav" style="left:326px;top:3474px">
    <span>Home</span><span>Therapy</span><span>What is it?</span><span>Types of therapy</span><span>Referral form</span>
  </nav>
  <div class="abs social" style="left:500px;top:3523px" role="img" aria-label="Social media links">
    <span></span><span></span><span></span><span></span>
  </div>
  <div class="abs" style="left:87px;top:3628px;width:1026px;height:1px;background:#4a4546"></div>
  <p class="abs" style="left:0;width:1200px;top:3646px;text-align:center;font-size:12.5px;font-weight:500;color:var(--white)">© COPYRIGHT 2022 | ALL RIGHTS RESERVED</p>
  <div class="abs" style="left:1129px;top:3588px;width:54px;height:54px;border-radius:50%;background:var(--teal);display:flex;align-items:center;justify-content:center">
    <svg width="28" height="24" viewBox="0 0 28 24"><path d="M14 2C7 2 2 6 2 11c0 2.6 1.4 5 3.7 6.6L4.5 22l5-2.6c1.4.4 2.9.6 4.5.6 7 0 12-4 12-9s-5-9-12-9Z" fill="#fff"/><circle cx="9" cy="11" r="1.6" fill="var(--teal)"/><circle cx="14" cy="11" r="1.6" fill="var(--teal)"/><circle cx="19" cy="11" r="1.6" fill="var(--teal)"/></svg>
  </div>
</footer>

</body>
</html>
```